Kitchen designer requires a website to showcase work

I require a simple website that will showcase designs, publications, and awards, about and contact. I have attached a couple of ideas that I have found (all kind of different) but we want to pitch this to the high end market, have a nice clean site with amazing images. The Website will be "Marcus Holloway Kitchen Design"

Industry/Entity Type

Kitchen

Coding

Coded - Design and coding required

Number of Pages Required

4 page

Requirements
Must have
• A content management system that I can manage myself

```html
<!DOCTYPE html>
<html lang="en">
<head>
<meta charset="utf-8">
<title>Marcus Holloway Kitchen Designs</title>
<link href="https://fonts.googleapis.com/css2?family=Open+Sans:wght@300;400&family=Questrial&display=swap" rel="stylesheet">
<style>
  :root {
    --header-bg: #1d1d1d;
    --nav-text: #d8d8d8;
    --white: #ffffff;
    --heading: #5a5a5a;
    --heading-dark: #3a3a3a;
    --muted: #8a8a8a;
    --band: #efefef;
    --rule: #d6d6d6;
    --card-text: #222222;
    --footer-text: #555555;
  }
  * { box-sizing: border-box; margin: 0; padding: 0; }
  html, body { width: 1182px; height: 1200px; overflow: hidden; background: var(--white); }
  body { font-family: "Open Sans", Arial, sans-serif; font-weight: 300; position: relative; }

  .site-header { height: 92px; background: var(--header-bg); position: relative; }
  .brand {
    position: absolute; left: 77px; top: 22px;
    font-family: "Questrial", "Century Gothic", sans-serif;
    color: var(--white); font-size: 20px; line-height: 24px; letter-spacing: 0.5px;
    text-transform: uppercase;
  }
  .brand span { display: block; }
  .brand span + span { padding-left: 48px; }
  .main-nav { position: absolute; right: 77px; top: 36px; display: flex; gap: 27px; }
  .main-nav a {
    font-family: "Questrial", "Century Gothic", sans-serif;
    font-size: 14.5px; letter-spacing: 0.8px; color: var(--nav-text);
    text-decoration: none; text-transform: uppercase;
  }
  .main-nav a.is-active { color: var(--white); }

  .hero {
    position: relative; height: 554px;
    background:
      radial-gradient(ellipse at 30% 30%, rgba(200,170,120,0.35), transparent 55%),
      linear-gradient(160deg, #5a4a3a 0%, #2a2320 35%, #7a6a5a 60%, #b8b0a8 85%, #d8d4cf 100%);
  }
  .hero-caption {
    position: absolute; left: 125px; top: 194px; width: 933px; height: 146px;
    background: rgba(20,20,20,0.55);
    color: var(--white); text-align: center;
    font-family: "Questrial", "Century Gothic", sans-serif;
  }
  .hero-caption .lead { font-size: 31px; margin-top: 12px; }
  .hero-caption .title { font-size: 41px; margin-top: 20px; letter-spacing: 0.5px; }
  .slider-dots { position: absolute; left: 554px; top: 512px; display: flex; gap: 8px; }
  .slider-dots span { width: 12px; height: 12px; border-radius: 50%; border: 1.5px solid var(--white); }
  .slider-dots span.is-current { background: #333; border-color: #333; }

  .welcome { height: 196px; text-align: center; padding-top: 48px; }
  .welcome h1 {
    font-family: "Questrial", "Century Gothic", sans-serif; font-weight: 400;
    font-size: 31px; color: var(--heading);
  }
  .welcome h1 em { color: var(--heading-dark); }
  .welcome p { margin: 22px auto 0; width: 520px; font-size: 17px; line-height: 23px; color: var(--muted); }

  .features { height: 318px; background: var(--band); border-top: 1px solid var(--rule); padding: 30px 0 0 77px; }
  .feature-grid { display: grid; grid-template-columns: repeat(4, 246px); gap: 15px; }
  .feature-card { height: 258px; }
  .feature-card.is-highlighted { background: var(--white); border-bottom: 1.5px solid #222; height: 258px; }
  .feature-image { height: 144px; }
  .feature-card p { padding: 9px 12px 0; font-size: 15.5px; line-height: 20.5px; color: var(--muted); }
  .feature-card.is-highlighted p { color: var(--card-text); font-weight: 400; }
  .img-white-kitchen { background: linear-gradient(180deg, #f4f4f2 0%, #d8dcd8 45%, #3a2a24 80%, #e8e8e8 100%); }
  .img-bright-kitchen { background: linear-gradient(180deg, #f2f2f0 0%, #d0cfc8 50%, #f0f0ee 100%); }
  .img-green-kitchen { background: linear-gradient(180deg, #7a7a60 0%, #d8d6cc 40%, #8cc43a 65%, #7ab02e 100%); }
  .img-vanity { background: linear-gradient(180deg, #6a6458 0%, #d8d2c4 45%, #c8c0b0 100%); }

  .site-footer { border-top: 1px solid var(--rule); height: 40px; padding: 12px 0 0 77px; }
  .site-footer p {
    font-family: "Questrial", "Century Gothic", sans-serif;
    font-size: 12.5px; color: var(--footer-text); text-transform: uppercase;
  }
  .site-footer p span { text-transform: none; }
</style>
</head>
<body>
  <header class="site-header">
    <div class="brand"><span>Marcus Holloway</span><span>Kitchen Designs</span></div>
    <nav class="main-nav">
      <a href="#" class="is-active">Home</a>
      <a href="#">Company Profile</a>
      <a href="#">Contact</a>
      <a href="#">Kitchens</a>
      <a href="#">Cupboards</a>
      <a href="#">Vanities</a>
    </nav>
  </header>

  <section class="hero" role="img" aria-label="Photograph of a modern kitchen with wood-grain cabinets, black granite counters and a mosaic floor">
    <div class="hero-caption">
      <p class="lead">Specialists in the design, construction, supply and fitment of</p>
      <p class="title">QUALITY KITCHENS</p>
    </div>
    <div class="slider-dots"><span class="is-current"></span><span></span><span></span><span></span></div>
  </section>

  <section class="welcome">
    <h1>Welcome to <em>MARCUS HOLLOWAY KITCHEN DESIGNS</em></h1>
    <p>Marcus Holloway Kitchen Designs cc has been serving the Gauteng community for over 20 years.</p>
  </section>

  <section class="features">
    <div class="feature-grid">
      <article class="feature-card is-highlighted">
        <div class="feature-image img-white-kitchen" role="img" aria-label="Photograph of a white open-plan kitchen with a dark island"></div>
        <p>We specialize in the design, manufacture and installation of beautiful kitchens, cupboards and vanities.</p>
      </article>
      <article class="feature-card">
        <div class="feature-image img-bright-kitchen" role="img" aria-label="Photograph of a bright white kitchen with a central island"></div>
        <p>Our friendly and professional staff is here to answer any questions you may have about our company or our services.</p>
      </article>
      <article class="feature-card">
        <div class="feature-image img-green-kitchen" role="img" aria-label="Photograph of a kitchen with lime green lower cabinets"></div>
        <p>Whether you need a completely new installation of your dream kitchen or a new vanity in your bathroom, we have what you need.</p>
      </article>
      <article class="feature-card">
        <div class="feature-image img-vanity" role="img" aria-label="Photograph of an ornate white double vanity with mirrors"></div>
        <p>At Marcus Holloway Kitchen Designs cc, our goal is to provide you with courteous, expedient, professional service of the highest caliber.</p>
      </article>
    </div>
  </section>

  <footer class="site-footer">
    <p>© Marcus Holloway Kitchen Designs 2015. <span>All rights reserved.</span></p>
  </footer>
</body>
</html>
```